4 Page Music Brochure design

We need assistance in designing a 4 Page A4 (A3 folded) Brochure promoting International Music Tour options for school groups. We have included text in the brief as well as images to be used in the brochure.

```html
<!DOCTYPE html>
<html lang="en">
<head>
<meta charset="utf-8">
<title>International Music Tours – Brochure Spread</title>
<link href="https://fonts.googleapis.com/css2?family=Fira+Sans+Condensed:wght@600&family=Fira+Sans:wght@300&display=swap" rel="stylesheet">
<style>
  :root {
    --paper: #ffffff;
    --maroon: #6b1d21;
    --ink-light: #f3e9e9;
    --rule: #ffffff;
  }
  html, body {
    margin: 0;
    padding: 0;
    width: 1200px;
    height: 1200px;
    overflow: hidden;
    background: var(--paper);
  }
  .canvas {
    position: relative;
    width: 1200px;
    height: 1200px;
    background: var(--paper);
  }
  .spread {
    position: absolute;
    left: 48px;
    top: 210px;
    width: 1104px;
    height: 780px;
    background: var(--maroon);
  }
  .photo {
    position: absolute;
  }
  .photo--ghent {
    left: 0; top: 0; width: 552px; height: 496px;
    background: linear-gradient(180deg, #a9bfd9 0%, #d6dde6 30%, #6f6a68 55%, #55504d 75%, #8e8b86 100%);
  }
  .photo--hall {
    left: 552px; top: 0; width: 278px; height: 184px;
    background: radial-gradient(ellipse at 50% 60%, #8a5a22 0%, #3c2412 45%, #120b07 100%);
  }
  .photo--gates {
    left: 552px; top: 200px; width: 278px; height: 184px;
    background: linear-gradient(90deg, #7a1608 0%, #e0421c 30%, #f06a3a 50%, #e0421c 70%, #7a1608 100%);
  }
  .photo--theatre {
    left: 552px; top: 400px; width: 278px; height: 182px;
    background: radial-gradient(ellipse at 40% 55%, #c99a4a 0%, #7a3a1c 45%, #2a0f08 100%);
  }
  .photo--band {
    left: 552px; top: 596px; width: 278px; height: 184px;
    background: linear-gradient(180deg, #8f8a86 0%, #6d6661 40%, #b5242a 65%, #2a1c1c 100%);
  }
  .tour {
    position: absolute;
    color: var(--ink-light);
  }
  .tour__title {
    margin: 0;
    font-family: "Fira Sans Condensed", sans-serif;
    font-weight: 600;
    font-size: 18px;
    line-height: 22px;
    color: #ffffff;
  }
  .tour__dates {
    margin: 0 0 6px;
    font-family: "Fira Sans", sans-serif;
    font-weight: 300;
    font-size: 16px;
    line-height: 22px;
    color: #ffffff;
  }
  .tour__text {
    margin: 6px 0 0;
    font-family: "Fira Sans", sans-serif;
    font-weight: 300;
    font-size: 11.3px;
    line-height: 17.6px;
  }
  .tour--choir { left: 21px; top: 513px; width: 380px; }
  .tour--choir .tour__title { margin-bottom: 0; }
  .tour--choir .tour__text { margin-top: 0; }
  .tour--hall    { left: 846px; top: 12px;  width: 250px; }
  .tour--japan   { left: 846px; top: 206px; width: 250px; }
  .tour--europe  { left: 847px; top: 405px; width: 250px; }
  .tour--usa     { left: 848px; top: 600px; width: 250px; }
  .rule {
    position: absolute;
    left: 846px;
    width: 246px;
    height: 2px;
    background: var(--rule);
  }
  .rule--1 { top: 183px; }
  .rule--2 { top: 383px; }
  .rule--3 { top: 581px; }
</style>
</head>
<body>
<div class="canvas">
  <section class="spread">
    <div class="photo photo--ghent" role="img" aria-label="Photo of a Flemish old town street with gothic church towers, a tram and pedestrians"></div>
    <div class="photo photo--hall" role="img" aria-label="Photo of a historic concert hall facade lit at night"></div>
    <div class="photo photo--gates" role="img" aria-label="Photo of a path through a tunnel of red-orange shrine gates"></div>
    <div class="photo photo--theatre" role="img" aria-label="Photo of an ornate opera house interior with an orchestra on stage"></div>
    <div class="photo photo--band" role="img" aria-label="Photo of a marching band in red and white uniforms parading down a city street"></div>

    <article class="tour tour--choir">
      <h2 class="tour__title">Global Choir Festival</h2>
      <p class="tour__dates">(5th to the 15th of July 2020)</p>
      <p class="tour__text">Join the biggest Choral Music event in the world with Choirs from over 80 different countries and regions, taking part in adjudicated performances, individual coaching, and singing workshops. Held in Belgium in the cities Antwerp and Ghent, this is a fantastic opportunity to perform on the world stage as well as take in the rich history of the Flanders region. With the option to extend your trip to include France, Germany, Italy, Austria or other nearby European Countries.</p>
    </article>

    <article class="tour tour--hall">
      <h2 class="tour__title">Harmon Hall</h2>
      <p class="tour__text">The once in a life time opportunity to perform on one of the world’s most famous music venues. Choirs will also have the opportunity to participate in performances, clinics, workshops, and exchanges. Based in New York City, there will also be the chance to include stops in Washington DC, Los Angeles, or San Francisco on to your trip.</p>
    </article>
    <div class="rule rule--1"></div>

    <article class="tour tour--japan">
      <h2 class="tour__title">Japan Music Tours</h2>
      <p class="tour__text">Travel to the land of the Rising Sun and take part in school exchanges, public performances and the chance to perform at iconic theme parks Tokyo Starland Park and Osaka Film World. Students will have the opportunity to take a Japanese Cooking Class, partake in a Traditional Japanese Tea Ceremony, see a Kabuki show, and ride the bullet train.</p>
    </article>
    <div class="rule rule--2"></div>

    <article class="tour tour--europe">
      <h2 class="tour__title">European Instrumental Tours</h2>
      <p class="tour__text">Play in Austria, France, Germany, the United Kingdom, or wherever your heart desires, your band, orchestra or ensemble will have the opportunity to perform at concert halls across Europe. As well as opportunities to participate in festivals, public performances and workshop with music professionals.</p>
    </article>
    <div class="rule rule--3"></div>

    <article class="tour tour--usa">
      <h2 class="tour__title">US Music Road Trip</h2>
      <p class="tour__text">Trace a path across the US journeying from Jazz to Blues to Soul onto Rock’n’Roll before finishing in Country Music capital of the world – Nashville. You will visit New Orleans, Memphis and Nashville where you will have the opportunity to perform at unique venues, undertake school exchanges and participate in workshops with musicians and professionals.</p>
    </article>
  </section>
</div>
</body>
</html>
```